R7M Horizon Business Card Design

We need a business card created for our New Business "R7M Horizon"<br/><br/>The business card design is up to you however the following information must be on the business card:<br/><br/>Front of the business card -<br/>Email :tobyw@r7mhorizon.nz<br/>Mobile: +64 (0) 22 4871 569<br/>Website: www.r7mhorizon.nz<br/>Card Owner Name: Tobias Wrenhall<br/>Company Title: Business Development Manager<br/>Slogan: "The BEST of both worlds". <br/>Logo On the front attached to the design brief<br/><br/>On the back: <br/>Space on the back for 4 more versions of the logo across the bottom of the card indicating different subsidiary brands - R7M Coffee, R7M Arts, R7M ?? (The card will be used for all of these brands - We Will add the extra subsidiary logos to the design once the design is finished (We are a graphics design team). <br/><br/>Other than that we want a premium feeling logo that remains universally usable depending on the business entity that we are using the card for. The use of bright bold colours would be great but we still want the card to feel premium.
Target Market(s)
Gift Design and Manufacturing Companies
Contact Information for Business Card
Front of the business card -
Email :tobyw@r7mhorizon.nz
Mobile: +64 (0) 22 4871 569
Website: www.r7mhorizon.nz
Card Owner Name: Tobias Wrenhall
Company Title: Business Development Manager
Slogan: "The BEST of both worlds".
Logo On the front attached to the design brief

```html
<!DOCTYPE html>
<html lang="en">
<head>
<meta charset="utf-8">
<title>R7M Horizon Business Card</title>
<link rel="stylesheet" href="https://fonts.googleapis.com/css2?family=Roboto:wght@300;400;700&display=swap">
<style>
  :root {
    --stage: #e8e8e8;
    --card-white: #ffffff;
    --card-dark: #2b2b2b;
    --brand-blue: #3340a8;
    --ink: #3a3a3a;
    --ink-soft: #555555;
    --rule: #8a8a8a;
    --back-name: #1f1f1f;
    --tagline: #d8d8d8;
  }
  * { box-sizing: border-box; margin: 0; padding: 0; }
  html, body {
    width: 1200px; height: 801px; overflow: hidden;
    background: var(--stage);
    font-family: "Roboto", Arial, sans-serif;
  }
  .stage {
    width: 1200px; height: 801px;
    display: flex; align-items: center; justify-content: center; gap: 60px;
  }
  .card {
    width: 520px; height: 297px;
    border-bottom: 4px solid var(--brand-blue);
    position: relative;
  }
  .card--front { background: var(--card-white); }
  .card--back { background: var(--card-dark); }

  /* Front */
  .front-top {
    position: absolute; left: 44px; right: 30px; top: 70px;
    display: flex; align-items: center;
  }
  .company-name {
    color: var(--brand-blue); font-weight: 700; font-size: 25px;
    width: 210px;
  }
  .divider { width: 1px; height: 70px; background: var(--rule); margin: 0 20px; }
  .contact-list { list-style: none; font-size: 13px; font-weight: 300; color: var(--ink); }
  .contact-list li { display: flex; align-items: center; gap: 9px; line-height: 22px; }
  .contact-list svg { width: 12px; height: 12px; flex: none; }
  .contact-list .accent { color: var(--brand-blue); }

  .person { position: absolute; left: 44px; top: 172px; }
  .person__name {
    color: var(--brand-blue); font-weight: 700; font-size: 19px;
    text-transform: uppercase; letter-spacing: 0.5px;
  }
  .person__role { color: var(--ink-soft); font-size: 15px; font-weight: 300; margin-top: 2px; padding-left: 120px; }
  .person__title { color: var(--ink); font-size: 14px; font-weight: 300; margin-top: 16px; }

  /* Back */
  .back-name {
    position: absolute; left: 0; right: 0; top: 98px;
    text-align: center;
    color: var(--back-name); font-weight: 700; font-size: 48px;
  }
  .tagline {
    position: absolute; left: 0; right: 0; top: 200px;
    text-align: center; color: var(--tagline);
    font-size: 16px; font-weight: 300;
  }
</style>
</head>
<body>
<main class="stage">
  <section class="card card--front" aria-label="Business card front">
    <div class="front-top">
      <p class="company-name">R7M Horizon</p>
      <div class="divider"></div>
      <ul class="contact-list">
        <li>
          <svg viewBox="0 0 24 24" fill="var(--brand-blue)"><path d="M6.6 10.8a15.1 15.1 0 0 0 6.6 6.6l2.2-2.2c.3-.3.7-.4 1-.2 1.1.4 2.3.6 3.6.6.6 0 1 .4 1 1V20c0 .6-.4 1-1 1C10.6 21 3 13.4 3 4c0-.6.4-1 1-1h3.5c.6 0 1 .4 1 1 0 1.2.2 2.4.6 3.6.1.3 0 .7-.2 1z"/></svg>
          <span>+64 (0) 22 4871 569</span>
        </li>
        <li>
          <svg viewBox="0 0 24 24" fill="none" stroke="var(--brand-blue)" stroke-width="2"><rect x="3" y="5" width="18" height="14" rx="1"/><path d="M3 6l9 7 9-7"/></svg>
          <span>tobyw@r7mhorizon.nz</span>
        </li>
        <li>
          <svg viewBox="0 0 24 24" fill="none" stroke="var(--brand-blue)" stroke-width="2"><circle cx="12" cy="12" r="9"/><path d="M3 12h18M12 3c3 3 3 15 0 18M12 3c-3 3-3 15 0 18"/></svg>
          <span>www.<span class="accent">r7mhorizon</span>.nz</span>
        </li>
      </ul>
    </div>
    <div class="person">
      <p class="person__name">Tobias Wrenhall</p>
      <p class="person__role">Owner</p>
      <p class="person__title">Business Development Manager</p>
    </div>
  </section>

  <section class="card card--back" aria-label="Business card back">
    <p class="back-name">R7M Horizon</p>
    <p class="tagline">The BEST of both worlds</p>
  </section>
</main>
</body>
</html>
```